MRB - Stationery Design Project

We need stationery based on our logo.

Company info :
Cabinet Morvalle & Associés
Société à responsabilité limitée au capital de 200.000 FCFP
RCS Papeete 27586D - Numéro tahiti C36927
Centre d’affaires OPALE - Rue Gaston Berthelin
BP 51839 MAISON VERDA - 98713 Papeete
Tahiti - Polynésie française
Tél : +689 40 63 17 94
Fax : +689 40 72 39 58

Industry/Entity Type

It Company

Font styles to use
Sans Serif

```html
<!DOCTYPE html>
<html lang="fr">
<head>
<meta charset="utf-8">
<title>Cabinet Morvalle &amp; Associés – Papier à en-tête</title>
<link rel="stylesheet" href="https://fonts.googleapis.com/css2?family=Questrial&display=swap">
<style>
  :root {
    --backdrop: #e9eaec;
    --paper: #ffffff;
    --navy: #1f3a5c;
    --slate: #6e7c86;
    --rule: #9aa3aa;
  }
  * { margin: 0; padding: 0; box-sizing: border-box; }
  html, body {
    width: 1200px;
    height: 936px;
    overflow: hidden;
    background: var(--backdrop);
    font-family: "Questrial", "Century Gothic", sans-serif;
  }
  .letterhead {
    position: absolute;
    left: 289px;
    top: 28px;
    width: 622px;
    height: 880px;
    background: var(--paper);
    box-shadow: 0 2px 10px rgba(0,0,0,0.08);
  }
  .brand {
    position: absolute;
    left: 62px;
    top: 64px;
    color: var(--navy);
  }
  .brand-name {
    font-size: 52px;
    line-height: 1;
    letter-spacing: 2px;
  }
  .brand-full {
    font-size: 13px;
    margin-top: 4px;
    letter-spacing: 0.3px;
  }
  .brand-tagline {
    font-size: 7px;
    margin-top: 2px;
    letter-spacing: 0.4px;
  }
  .footer {
    position: absolute;
    left: 62px;
    right: 62px;
    bottom: 52px;
    text-align: right;
    font-size: 8.5px;
    line-height: 1.55;
    color: var(--slate);
  }
  .footer .label { color: var(--navy); font-weight: bold; }
  .footer-rule {
    border: 0;
    border-top: 1px solid var(--rule);
    margin: 8px 0 6px;
  }
  .footer-legal {
    font-size: 7.5px;
    text-align: center;
  }
</style>
</head>
<body>
  <main class="letterhead">
    <header class="brand">
      <div class="brand-name">MRB</div>
      <div class="brand-full">Cabinet Morvalle &amp; Associés</div>
      <div class="brand-tagline">Expertise comptable · Audit · Conseil</div>
    </header>

    <footer class="footer">
      <p class="footer-address">Centre d’affaires OPALE - Rue Gaston Berthelin, BP 51839 MAISON VERDA - 98713 Papeete, Tahiti - Polynésie française</p>
      <p class="footer-contact"><span class="label">Tél</span> : +689 40 63 17 94 &nbsp;<span class="label">Fax</span> : +689 40 72 39 58</p>
      <hr class="footer-rule">
      <p class="footer-legal">Société à responsabilité limitée au capital de 200.000 FCFP - RCS Papeete 27586D - Numéro tahiti C36927</p>
    </footer>
  </main>
</body>
</html>
```